Packaging label for launch of sun dried tomato products.

Established family farm in South Africa growing fruit for the production of dried fruit. We need a packaging label for the launch of our sun dried tomato products ie dried tomatoes in olive oil, dried tomato flakes and tomato powder. Packaging will be a round glass "jam jar" and spice shaker bottle. Due to limited amount of product available we cannot market to the masses, but rather focus on conveying a message of quality and exclusivity.

Target Market(s)

Home chef

Industry/Entity Type

Food

Font styles to use
Serif

Requirements
Nice to have
• Include the farm name in the design. TAVSONE

```html
<!DOCTYPE html>
<html lang="en">
<head>
<meta charset="utf-8">
<title>Tavsone – Sun Dried Tomato Labels</title>
<link rel="stylesheet" href="https://fonts.googleapis.com/css2?family=Alegreya+SC:wght@700;800&family=Lexend:wght@400&family=Oswald:wght@400&display=swap">
<style>
  :root {
    --paper: #ffffff;
    --cream: #f2d19e;
    --tomato-red: #c0343c;
    --tomato-orange: #ee6b43;
    --leaf-green: #2e6b22;
  }
  html, body {
    margin: 0;
    padding: 0;
    width: 1200px;
    height: 1200px;
    overflow: hidden;
    background: var(--paper);
  }
  .label-sheet {
    display: block;
    width: 1200px;
    height: 1200px;
  }
  .label-base { fill: var(--cream); }
  .rule-red { fill: none; stroke: var(--tomato-red); stroke-width: 7; }
  .rule-green { fill: none; stroke: var(--leaf-green); stroke-width: 8; }
  .brand-name {
    font-family: "Alegreya SC", Georgia, serif;
    font-weight: 800;
    fill: var(--tomato-red);
    text-anchor: middle;
  }
  .tagline {
    font-family: "Lexend", Arial, sans-serif;
    font-weight: 400;
    fill: var(--leaf-green);
    text-anchor: middle;
    letter-spacing: 0.04em;
  }
  .net-weight {
    font-family: "Oswald", "Arial Narrow", sans-serif;
    fill: var(--leaf-green);
    text-anchor: middle;
    letter-spacing: 0.06em;
  }
  .origin {
    font-family: "Oswald", "Arial Narrow", sans-serif;
    text-anchor: middle;
    letter-spacing: 0.06em;
  }
  .origin--red { fill: var(--tomato-orange); }
  .origin--green { fill: var(--leaf-green); }
  .product-name {
    font-family: "Alegreya SC", Georgia, serif;
    font-weight: 700;
    fill: var(--tomato-red);
    text-anchor: middle;
    letter-spacing: 0.05em;
  }
</style>
</head>
<body>
<svg class="label-sheet" viewBox="0 0 1932 1932" xmlns="http://www.w3.org/2000/svg">
  <defs>
    <radialGradient id="tomato-fill" cx="50%" cy="50%" r="55%">
      <stop offset="0" stop-color="#ee6b43"/>
      <stop offset="1" stop-color="#c0343c"/>
    </radialGradient>
    <path id="front-origin-curve" d="M290 1430 Q535 1515 780 1430"/>
    <path id="side-origin-curve" d="M1385 1335 Q1555 1385 1725 1335"/>
  </defs>

  <!-- Front jar label -->
  <g class="label label--front">
    <path class="label-base" d="M245 452 Q535 340 825 452 L825 505 L933 505 L933 1407 L825 1407 L825 1458 Q535 1575 245 1458 L245 1407 L137 1407 L137 505 L245 505 Z"/>
    <path class="rule-red" d="M255 462 Q535 360 815 462 L815 516 L923 516 L923 1396 L815 1396 L815 1450 Q535 1555 255 1450 L255 1396 L147 1396 L147 516 L255 516 Z"/>
    <path class="rule-green" d="M272 472 Q535 385 798 472 L798 537 L903 537 L903 1376 L798 1376 L798 1436 Q535 1535 272 1436 L272 1376 L168 1376 L168 537 L272 537 Z"/>
    <path class="rule-red" d="M200 600 L200 563 L250 563 M820 563 L870 563 L870 600 M200 720 L200 1347 L372 1347 M698 1347 L870 1347 L870 720"/>

    <text class="brand-name" x="535" y="695" font-size="140">TAVSONE</text>
    <text class="tagline" x="535" y="835" font-size="60">PREMIUM QUALITY</text>

    <rect role="img" aria-label="Illustration of three ripe red tomatoes with green stems" x="225" y="890" width="630" height="400" rx="200" fill="url(#tomato-fill)"/>

    <text class="net-weight" x="535" y="1364" font-size="38">NET WEIGHT : 500ML</text>
    <text class="origin origin--red" font-size="46">
      <textPath href="#front-origin-curve" startOffset="50%">MADE IN SOUTH AFRICA</textPath>
    </text>
  </g>

  <!-- Spice shaker label -->
  <g class="label label--shaker">
    <path class="label-base" d="M1345 535 L1425 535 Q1555 420 1690 535 L1765 535 L1765 1415 L1690 1415 Q1555 1550 1425 1415 L1345 1415 Z"/>
    <path class="rule-red" d="M1357 548 L1430 548 Q1555 448 1685 548 L1753 548 L1753 1402 L1685 1402 Q1555 1525 1430 1402 L1357 1402 Z"/>

    <rect role="img" aria-label="Small illustration of three red tomatoes" x="1483" y="545" width="152" height="90" rx="45" fill="url(#tomato-fill)"/>

    <text class="brand-name" x="1555" y="740" font-size="82">TAVSONE</text>
    <text class="tagline" x="1555" y="793" font-size="27">PREMIUM QUALITY</text>

    <text class="product-name" x="1555" y="1038" font-size="56">TOMATO</text>
    <text class="product-name" x="1555" y="1085" font-size="56">POWDER</text>

    <text class="origin origin--green" font-size="34">
      <textPath href="#side-origin-curve" startOffset="50%">MADE IN SOUTH AFRICA</textPath>
    </text>
  </g>
</svg>
</body>
</html>
```